依頼概要
■依頼の目的/概要
夢をかなえる人だけが気づいている「月の舟の旅」の秘密の味わい方のデザインをお願いします。

■本の内容
詳しくは添付ファイルを読んでいただいてデザインをお願いします。
シンデレラ物語は実は現実の物語で、成功に導く内容が含まれているものだったという内容になります。

■デザイン要望
明るいもの、好印象が持てるようなものがいいかと思っています。
その他何かご不明な点がございましたら、お気軽にご質問下さい。
よろしくお願いいたします。
夢をかなえる人だけが気づいている「月の舟の旅」の秘密の味わい方
は電子書籍です。
著者名は タケル K  です。
ご提案誠にありがとうございます。

デザイン上支障がない場合には

読者様限定

シンデレラ度チェックシート

プレゼント

などの文言を入れてみてもらってもよいでしょうか?
■ 選んだ理由

数多くの素敵な提案ありがとうございました。
私だけでは決めかねて迷うほどでしたので、知人、電子書籍出版グループのメンバーに意見(投票)を伺いながら決定しました。
その際
〇シンデレラの世界観に沿ったデザインの雰囲気、わかりやすさ
〇中央下のガラスの靴のインパクト
〇文中からの言葉
などが高評価となっていましたので、決めさせていただきました。

■ 提案者全員のお礼・コメント

この度は、数多くの素敵な提案をいただき誠にありがとうございました。
感謝いたしております。
皆様方の今後のご活躍を願っております。
またご縁がございましたら、その節はよろしくお願い申し上げます。

```html
<!DOCTYPE html>
<html lang="ja">
<head>
<meta charset="UTF-8">
<title>夢をかなえる人だけが気づいている「月の舟の旅」の秘密の味わい方</title>
<link rel="stylesheet" href="https://fonts.googleapis.com/css2?family=M+PLUS+Rounded+1c:wght@400;500;700;800&display=swap">
<style>
  :root {
    --paper: #ffffff;
    --red: #d9232e;
    --heart: #e8332a;
    --light-cream: #f3f1ec;
    --soft-yellow: #f2d56a;
    --deep-red: #c8262c;
  }
  * { margin: 0; padding: 0; box-sizing: border-box; }
  html, body {
    width: 749px; height: 1200px; overflow: hidden; background: var(--paper);
  }
  .cover {
    position: relative; width: 749px; height: 1200px; background: var(--paper);
    font-family: "M PLUS Rounded 1c", sans-serif; color: var(--red);
  }
  .cover-frame {
    position: absolute; inset: 13px; border: 3px solid var(--red);
  }
  .title {
    position: absolute; top: 80px; left: 0; right: 0; text-align: center;
    font-weight: 500; line-height: 1;
  }
  .title span { display: block; white-space: nowrap; }
  .title-line { font-size: 60px; margin-bottom: 18px; }
  .title-key {
    font-size: 68px; font-weight: 800; margin: 4px 0 18px; letter-spacing: 1px;
  }
  .heart {
    position: absolute; left: 320px; top: 470px; width: 110px; height: 100px;
  }
  .illustration {
    position: absolute; border-radius: 40px 40px 20px 20px;
  }
  .illustration-left {
    left: 145px; top: 610px; width: 185px; height: 325px;
    background: linear-gradient(180deg, var(--soft-yellow) 0%, #f7e7b8 25%, var(--light-cream) 55%, #e9e6df 100%);
  }
  .illustration-right {
    left: 410px; top: 635px; width: 180px; height: 290px;
    background: linear-gradient(180deg, #e8c889 0%, #f1d3b5 28%, var(--deep-red) 50%, #a61e23 100%);
  }
  .author {
    position: absolute; left: 425px; top: 1010px; text-align: left;
  }
  .author-role { display: block; font-size: 24px; font-weight: 500; }
  .author-name { display: block; font-size: 44px; font-weight: 800; margin-top: 8px; white-space: nowrap; }
</style>
</head>
<body>
  <main class="cover">
    <div class="cover-frame"></div>

    <h1 class="title">
      <span class="title-line">夢をかなえる人だけが</span>
      <span class="title-line">気づいている</span>
      <span class="title-key">「月の舟の旅」</span>
      <span class="title-line">の秘密の味わい方</span>
    </h1>

    <svg class="heart" viewBox="0 0 110 100" aria-hidden="true">
      <defs>
        <filter id="heart-glow" x="-30%" y="-30%" width="160%" height="160%">
          <feGaussianBlur stdDeviation="4"/>
        </filter>
      </defs>
      <path d="M55 92 C20 66 8 48 10 32 C12 16 26 8 38 10 C47 12 52 18 55 26 C58 18 63 12 72 10 C84 8 98 16 100 32 C102 48 90 66 55 92 Z"
            fill="var(--heart)" opacity="0.5" filter="url(#heart-glow)"/>
      <path d="M55 86 C24 63 16 48 18 34 C20 21 31 15 40 17 C47 19 52 24 55 31 C58 24 63 19 70 17 C79 15 90 21 92 34 C94 48 86 63 55 86 Z"
            fill="var(--heart)"/>
    </svg>

    <div class="illustration illustration-left" role="img" aria-label="白い服を着た女の子のイラスト"></div>
    <div class="illustration illustration-right" role="img" aria-label="赤い服の男の子が小さな贈り物を差し出すイラスト"></div>

    <p class="author">
      <span class="author-role">（作家／コーチ）</span>
      <span class="author-name">タケル K</span>
    </p>
  </main>
</body>
</html>
```